Zielgruppe
Was soll 'verkauft' werden?
Das Theaterstück „Das Sternenfloß am langen Nachmittag“, welches an verschiedenen Orten aufgeführt werden soll.
Zielgruppe:
Der Flyer wird zusammen mit einem Anschreiben und einem kleinen Give-Away (Ideen zur Mechanik und dem Give-Away sehr willkommen!) per Post und E-Mail bundesweit primär an Schulen und andere potentielle Theater-Aufführungsorte (Bibliotheken, Kulturvereine, etc.) versendet. Die Zielgruppe sind somit Entscheider in Schulen, die über eine Schulaufführung entscheiden können bzw. andere Entscheider, die über Theater-Aufführungen an obigen Orten entscheiden können. Nach dem Versand wird mittels eines Telefonanrufs „nachgefasst“, ob das Mailing „gut“ angekommen ist und ob ein weitergehendes Interesse besteht.
Siehe auch Briefingdokument.
Aufgabenstellung
Erstellung eines 4-seitigen Flyers (Formatwunsch: DIN lang oder ähnlich).

```html
<!DOCTYPE html>
<html lang="de">
<head>
<meta charset="utf-8">
<title>Das Sternenfloß – Flyer DIN lang</title>
<link rel="stylesheet" href="https://fonts.googleapis.com/css2?family=Carlito&family=Roboto+Condensed:ital,wght@0,400;0,700;1,400;1,700&display=swap">
<style>
  :root {
    --paper: #ffffff;
    --ink: #111111;
    --frame: #c8c8c8;
    --frame-dark: #999999;
    --band: #dcdcdc;
    --night: #0c0c0c;
    --label: #1a1a1a;
    --brand: #1d3f7a;
  }
  * { box-sizing: border-box; margin: 0; padding: 0; }
  html, body {
    width: 1200px; height: 600px; overflow: hidden;
    background: var(--paper);
  }
  .canvas { position: relative; width: 1200px; height: 600px; }

  .page-label {
    position: absolute; top: 53px;
    font-family: "Carlito", sans-serif; font-size: 22px; color: var(--label);
  }
  .page-label--front { left: 104px; }
  .page-label--inside { left: 369px; }
  .page-label--back { left: 874px; }

  .page {
    position: absolute; top: 86px; height: 475px;
    background: var(--paper); border: 1px solid var(--frame); overflow: hidden;
    font-family: "Roboto Condensed", sans-serif; color: var(--ink);
  }
  .page--front { left: 102px; top: 84px; width: 232px; border-color: var(--frame-dark); }
  .page--inside { left: 369px; width: 475px; }
  .page--back { left: 877px; width: 231px; }

  .shape { position: absolute; left: 0; top: 0; }

  /* Vorderseite */
  .front-title {
    position: absolute; top: 34px; left: 0; width: 100%;
    text-align: center; font-weight: 700; font-size: 25px; letter-spacing: -0.4px;
    transform: scaleY(1.2);
  }
  .front-artwork {
    position: absolute; top: 82px; left: 0; width: 100%; height: 256px;
    background: radial-gradient(ellipse at 55% 40%, #3a3a3a 0%, var(--night) 65%);
  }
  .front-claim {
    position: absolute; top: 294px; left: 0; width: 100%;
    text-align: center; color: var(--paper); font-weight: 700; font-size: 13px; line-height: 16px;
  }
  .front-photo {
    position: absolute; top: 338px; left: 0; width: 100%; height: 137px;
    background: linear-gradient(180deg, #2b2420 0%, #6a5648 45%, #8a7a70 100%);
  }

  /* Innenseiten */
  .section-title { font-weight: 700; font-size: 9.5px; margin-bottom: 12px; }
  .copy { font-size: 8.6px; line-height: 10.8px; }
  .copy + .copy { margin-top: 10px; }
  .block { position: absolute; }
  .block--play { left: 16px; top: 24px; width: 214px; }
  .block--duo { left: 16px; top: 396px; width: 214px; }
  .block--about { left: 247px; top: 228px; width: 216px; }
  .web { font-size: 8.6px; margin-top: 12px; }
  .quote { position: absolute; font-style: italic; font-size: 8.6px; line-height: 10.8px; }
  .quote--inside { left: 330px; top: 446px; width: 135px; }

  /* Rückseite */
  .contact { position: absolute; left: 30px; top: 244px; width: 185px; font-size: 8.6px; line-height: 10.8px; }
  .contact .section-title { font-size: 9px; margin-bottom: 14px; }
  .contact p + p { margin-top: 14px; }
  .quote--back { left: 22px; top: 378px; width: 192px; font-weight: 700; }
  .quote--back .source { display: block; font-weight: 400; margin-top: 8px; }
  .brand {
    position: absolute; right: 14px; bottom: 22px;
    display: flex; align-items: center; gap: 4px;
    font-weight: 700; font-size: 11px; color: var(--brand);
  }
  .brand-dot { width: 10px; height: 10px; border-radius: 50%; background: var(--brand); }
</style>
</head>
<body>
<main class="canvas">

  <span class="page-label page-label--front">Vorderseite</span>
  <span class="page-label page-label--inside">Innenseiten</span>
  <span class="page-label page-label--back">Rückseite</span>

  <!-- Vorderseite -->
  <section class="page page--front">
    <h1 class="front-title">DAS STERNENFLOSS</h1>
    <div class="front-artwork" role="img" aria-label="Schwarz-weiße Grafik einer Heldenfigur und eines Fabelwesens im Scherenschnitt-Stil"></div>
    <p class="front-claim">Die große deutsche Sage<br>kommt in die Schule</p>
    <div class="front-photo" role="img" aria-label="Foto einer Aufführung in einer Aula vor vielen Schülerinnen und Schülern"></div>
  </section>

  <!-- Innenseiten -->
  <section class="page page--inside">
    <svg class="shape" width="475" height="475" viewBox="0 0 475 475" aria-hidden="true">
      <polygon points="243,475 475,403 475,475" fill="var(--band)"/>
    </svg>

    <svg class="shape" width="475" height="475" viewBox="0 0 475 475" role="img" aria-label="Foto: Aufführung in einer Turnhalle, Publikum sitzt im Halbkreis auf dem Boden">
      <defs>
        <linearGradient id="gymTone" x1="0" y1="0" x2="1" y2="1">
          <stop offset="0" stop-color="#5a6470"/>
          <stop offset="0.5" stop-color="#b89a78"/>
          <stop offset="1" stop-color="#8a6a4a"/>
        </linearGradient>
      </defs>
      <polygon points="0,228 217,187 217,338 0,388" fill="url(#gymTone)"/>
    </svg>

    <svg class="shape" width="475" height="475" viewBox="0 0 475 475" role="img" aria-label="Porträtfoto des Schauspielers Aron Kessel">
      <defs>
        <linearGradient id="portraitTone" x1="0" y1="0" x2="0" y2="1">
          <stop offset="0" stop-color="#3f5a34"/>
          <stop offset="0.5" stop-color="#8a6a55"/>
          <stop offset="1" stop-color="#e8e6e2"/>
        </linearGradient>
      </defs>
      <polygon points="325,37 475,0 475,186 325,224" fill="url(#portraitTone)"/>
    </svg>

    <div class="block block--play">
      <h2 class="section-title">DAS THEATERSTÜCK</h2>
      <p class="copy">Erzählt wird die spannende Geschichte einer langen Reise: Mira und ihr Bruder bauen aus Treibholz ein Floß, treiben einen Nachmittag lang den großen Fluss hinab und begegnen dabei seltsamen Gestalten, einem verborgenen Schatz, einer alten Fährfrau und ihrer Angst vor der Nacht, die letztendlich zur größten Prüfung wird…</p>
      <p class="copy">Besonders ist diese Inszenierung für die Klassenstufen 5–10 und die ganze Familie geeignet, aber auch für ein rein erwachsenes Publikum. Aron Kessel spielt alle 13 Rollen und verändert hierbei nur die Körperlichkeit und Stimme.</p>
    </div>

    <div class="block block--duo">
      <p class="copy">Aron Kessel präsentiert mit einer Kollegin große Weltliteratur in knackigen 50 Minuten als 2-Personen-Lesung/Hörspiel. Geeignet für alle ab Klasse 10 und alle, die den „Faust“ schon immer verstehen wollten.</p>
    </div>

    <div class="block block--about">
      <h2 class="section-title">ÜBER ARON KESSEL</h2>
      <p class="copy">Aron Kessel ist ausgebildeter Schauspieler, Autor/Historienforscher und Sprecher. Er arbeitete u. a. an der Landesbühne Falkenau und am Stadttheater Oberwiesen. Außerdem steht er auch erfolgreich vor der Kamera (u. a. Spurensache, Zwei auf Streife etc.). Weiterhin schreibt und bearbeitet er Theaterstücke und Hörspiele (z. B. Das Sternenfloß für Radio Weststrom) mit dem Ziel, bedeutende Literatur, historische Ereignisse und Biografien jedermann zugänglich zu machen. Zuletzt schrieb und präsentierte er im Auftrag des Landesparlaments Talmark zum Antrittsbesuch des Bundespräsidenten Konrad Helmbrecht das Stück „Die Uferrepublik“.</p>
      <p class="web">www.aronkessel-beispiel.de</p>
    </div>

    <p class="quote quote--inside">„Eine Kurzfassung, die begeistert.“ (Neckartaler Anzeiger)</p>
  </section>

  <!-- Rückseite -->
  <section class="page page--back">
    <svg class="shape" width="231" height="475" viewBox="0 0 231 475" aria-hidden="true">
      <polygon points="0,364 231,313 231,475 0,475" fill="var(--band)"/>
    </svg>
    <svg class="shape" width="231" height="475" viewBox="0 0 231 475" role="img" aria-label="Porträtfoto: der Schauspieler blickt über ein aufgeschlagenes gelbes Taschenbuch">
      <defs>
        <linearGradient id="readerTone" x1="0" y1="0" x2="0" y2="1">
          <stop offset="0" stop-color="#9aa0a8"/>
          <stop offset="0.45" stop-color="#b08a70"/>
          <stop offset="0.75" stop-color="#e2c94a"/>
          <stop offset="1" stop-color="#3a5a8a"/>
        </linearGradient>
      </defs>
      <polygon points="0,0 231,0 231,168 0,224" fill="url(#readerTone)"/>
    </svg>

    <div class="contact">
      <h2 class="section-title">Kontakt- und Feedbackdaten</h2>
      <p>Aron Kessel<br>info@aronkessel-beispiel.de<br>06131-5527140</p>
      <p>www.aronkessel-beispiel.de</p>
    </div>

    <p class="quote quote--back">„Es liegt am mitreißenden Schauspieler Aron Kessel, der in Sekundenbruchteilen zwischen den insgesamt 13 Rollen hin- und herspringt, dass die Schüler so fasziniert sind.“<span class="source">(Hochwald-Kurier)</span></p>

    <div class="brand"><span class="brand-dot"></span>ARON KESSEL</div>
  </section>

</main>
</body>
</html>
```